App Design - Job Poise Lantern

We require an App Design for our new App called 'Poise Lantern'. This app is essentially an assistant to help Users prepare for job interviews, to help them get hired. <br/><br/>Users who download the App can view common Questions and Answers, save their favourite responses and also view common Interview Tips. <br/><br/>The vision for our App is for Users who are preparing for an interview (1 week before, 1 day before, even 1 hour before), are able to download, view and educate themselves on common questions and responses, and then be confident to land the job. <br/><br/>Our team has developed wireframes to help highlight what each screen should do and include. Please see attached document, which also highlights key requirements for the experience. Feel free to add/remove/edit what you see on these wireframes. Our preference is that you use Adobe XD please.<br/><br/>In terms of design guidelines, we want the experience to be simple, intuitive and 'memorable' to help Users to remember the questions/responses when they are in the interview. <br/><br/>The final design should communicate 'neat and clean professionalism'; we like the design of: vocatia hub com au<br/><br/>Thank you for reading! Good luck !

Target Market(s)

Professional job seekers

Font styles to use
Sans Serif

Colors

Designer to choose colors to be used in the design.

Requirements
Must have
• Please see my PixelBazaar_UX file that I have uploaded
Nice to have
• Could you also please include some ideas on how we can incorporate Advertising into the app screens

```html
<!DOCTYPE html>
<html lang="en">
<head>
<meta charset="utf-8">
<title>Poise Lantern – View Question &amp; Response</title>
<link href="https://fonts.googleapis.com/css2?family=Poppins:wght@400;500;600;700&display=swap" rel="stylesheet">
<style>
  :root {
    --canvas: #ffffff;
    --screen-bg: #f9f9f9;
    --green-light: #86ff12;
    --green-deep: #13f600;
    --green-line: #7ff03a;
    --text-dark: #1c1c1c;
    --text-caption: #5a5a5a;
    --white: #ffffff;
    --heart-red: #f50000;
  }
  * { box-sizing: border-box; margin: 0; padding: 0; }
  html, body {
    width: 1200px; height: 1199px; overflow: hidden;
    background: var(--canvas);
    font-family: "Poppins", sans-serif;
    color: var(--text-dark);
  }
  .app-screen {
    position: absolute; left: 350px; top: 84px;
    width: 499px; height: 948px;
    background: var(--screen-bg);
    border-radius: 46px;
    overflow: hidden;
    box-shadow: 0 0 0 1px #ececec;
  }
  .app-header {
    position: absolute; left: 0; top: 0; width: 100%; height: 134px;
    background: linear-gradient(90deg, var(--green-light), var(--green-deep));
  }
  .status-time {
    position: absolute; left: 40px; top: 10px;
    font-weight: 700; font-size: 16px; color: var(--text-dark);
  }
  .status-icons { position: absolute; right: 48px; top: 12px; }
  .back-button { position: absolute; left: 22px; top: 64px; }
  .app-title {
    position: absolute; left: 0; width: 100%; top: 62px;
    text-align: center; font-weight: 700; font-size: 30px;
    color: var(--white); letter-spacing: 0.2px;
  }
  .question-card {
    position: absolute; left: 0; top: 134px; width: 100%; height: 161px;
    background: var(--white);
    border: 1.5px solid var(--green-line); border-top: none;
    border-radius: 0 0 16px 16px;
    box-shadow: 0 6px 12px rgba(0,0,0,0.06);
  }
  .question-text {
    position: absolute; left: 40px; right: 40px; top: 30px;
    text-align: center; font-size: 16px; line-height: 20.5px;
  }
  .pager-arrow { position: absolute; top: 65px; }
  .pager-prev { left: 12px; }
  .pager-next { right: 12px; }
  .response-card {
    position: absolute; left: 28px; width: 448px; height: 188px;
    background: var(--white);
    border: 1.5px solid var(--green-line);
    border-radius: 14px;
    box-shadow: 0 6px 12px rgba(0,0,0,0.07);
  }
  .response-card:nth-of-type(1) { top: 314px; }
  .response-card:nth-of-type(2) { top: 521px; }
  .response-card:nth-of-type(3) { top: 728px; }
  .response-text {
    position: absolute; left: 10px; right: 10px; top: 25px;
    text-align: center; font-size: 16px; line-height: 20.5px;
  }
  .favourite-icon { position: absolute; left: 206px; top: 145px; }
  .screen-caption {
    position: absolute; left: 0; width: 100%; top: 1086px;
    text-align: center; font-size: 31px; font-weight: 400;
    color: var(--text-caption);
  }
</style>
</head>
<body>
  <main class="app-screen">
    <header class="app-header">
      <span class="status-time">05:30 AM</span>
      <svg class="status-icons" width="72" height="20" viewBox="0 0 72 20" aria-label="Signal and battery">
        <rect x="0" y="12" width="3" height="5" fill="#1c1c1c"/>
        <rect x="5" y="9" width="3" height="8" fill="#1c1c1c"/>
        <rect x="10" y="6" width="3" height="11" fill="#1c1c1c"/>
        <rect x="15" y="3" width="3" height="14" fill="#1c1c1c"/>
        <rect x="28" y="2" width="38" height="16" rx="8" fill="none" stroke="#1c1c1c" stroke-width="2"/>
        <rect x="67" y="7" width="3" height="6" rx="1" fill="#1c1c1c"/>
        <text x="47" y="15" text-anchor="middle" font-family="Poppins, sans-serif" font-weight="700" font-size="12" fill="#1c1c1c">50</text>
      </svg>
      <svg class="back-button" width="40" height="36" viewBox="0 0 40 36" aria-label="Back">
        <path d="M36 18H6M18 5L5 18l13 13" fill="none" stroke="#ffffff" stroke-width="5" stroke-linecap="round" stroke-linejoin="round"/>
      </svg>
      <h1 class="app-title">Poise Lantern</h1>
    </header>

    <section class="question-card">
      <svg class="pager-arrow pager-prev" width="14" height="28" viewBox="0 0 14 28" aria-label="Previous question">
        <path d="M14 0V28L0 14Z" fill="#7cf01c"/>
      </svg>
      <p class="question-text">1. Lorem ipsum dolor sit amet,consectetur adipisi<br>cing elit. Error quam vero, voluptatibusquaerat<br>minus blanditiis! Odio quo, ratione, magnam<br>quia fuga quae earum! Voluptate totamiure<br>expedita blanditiis nesciunt recusandae.</p>
      <svg class="pager-arrow pager-next" width="14" height="28" viewBox="0 0 14 28" aria-label="Next question">
        <path d="M0 0V28L14 14Z" fill="#7cf01c"/>
      </svg>
    </section>

    <article class="response-card">
      <p class="response-text">Lorem ipsum dolor sit amet,consectetur adipisi<br>cing elit. Error quam vero, voluptatibusquaerat<br>minus blanditiis! Odio quo, ratione, magnam<br>quia fuga quae earum! Voluptate totamiure<br>expedita blanditiis nesciunt recusandae.</p>
      <svg class="favourite-icon" width="36" height="32" viewBox="0 0 36 32" aria-label="Saved favourite">
        <path d="M18 31L3.5 16.5C-0.5 12.5 0 5.5 5 2.5 9.5 0 14.5 1.5 18 6 21.5 1.5 26.5 0 31 2.5 36 5.5 36.5 12.5 32.5 16.5Z" fill="#f50000"/>
      </svg>
    </article>

    <article class="response-card">
      <p class="response-text">Lorem ipsum dolor sit amet,consectetur adipisi<br>cing elit. Error quam vero, voluptatibusquaerat<br>minus blanditiis! Odio quo, ratione, magnam<br>quia fuga quae earum! Voluptate totamiure<br>expedita blanditiis nesciunt recusandae.</p>
      <svg class="favourite-icon" width="36" height="32" viewBox="0 0 36 32" aria-label="Save as favourite">
        <path d="M18 30L4.2 16.2C0.6 12.6 1 6.2 5.6 3.4 9.8 1 14.6 2.4 18 6.8 21.4 2.4 26.2 1 30.4 3.4 35 6.2 35.4 12.6 31.8 16.2Z" fill="none" stroke="#1c1c1c" stroke-width="1.6" stroke-linejoin="round"/>
      </svg>
    </article>

    <article class="response-card">
      <p class="response-text">Lorem ipsum dolor sit amet,consectetur adipisi<br>cing elit. Error quam vero, voluptatibusquaerat<br>minus blanditiis! Odio quo, ratione, magnam<br>quia fuga quae earum! Voluptate totamiure<br>expedita blanditiis nesciunt recusandae.</p>
      <svg class="favourite-icon" width="36" height="32" viewBox="0 0 36 32" aria-label="Save as favourite">
        <path d="M18 30L4.2 16.2C0.6 12.6 1 6.2 5.6 3.4 9.8 1 14.6 2.4 18 6.8 21.4 2.4 26.2 1 30.4 3.4 35 6.2 35.4 12.6 31.8 16.2Z" fill="none" stroke="#1c1c1c" stroke-width="1.6" stroke-linejoin="round"/>
      </svg>
    </article>
  </main>

  <p class="screen-caption">View Question &amp; Response</p>
</body>
</html>
```